Business Card & Email Signature Design || Upmarket + Luxury

Riverlume Honey, a New Zealand Manuka Honey company needs a Business Card & Email Signature design.

Our logo's are attached in Gold & Black versions, feel free to be creative with how you use the logo and it's patterns in your design.

Style:
- Looking for an Elegant, Luxurious, Upmarket feel.
- Black/Matte Black Card, Gold Foil, UV Embossing

Information to Add:

- Logo
- Company Name: Riverlume Honey
- Name: Mattias Brovell
- Title: Creative Director
- Phone: +64 2919 58 617
- Email: mattias@riverlumehoney.example
- Website: www.riverlumehoney.example

- Socials: ***For email Signature Only***
- Facebook: https://www.facebook.com/riverlumehoney/
- Instagram: https://www.instagram.com/riverlumehoney/

Target Market(s)

Asia/Europe Luxury, Upmarket

Contact Information for Business Card

- Logo
- Name: Mattias Brovell
- Phone: +64 2919 58 617

Font styles to use
Other font styles liked:
• Champagne & Limousines (Attached)

Requirements
Must have
• Business Card & Email Signature Design.

Looking for a Sleek, Luxury, Upmarket Design.

```html
<!DOCTYPE html>
<html lang="en">
<head>
<meta charset="utf-8">
<title>Riverlume Honey — Business Card</title>
<link href="https://fonts.googleapis.com/css2?family=Josefin+Sans:wght@300;400;600&display=swap" rel="stylesheet">
<style>
  :root {
    --backdrop: #f1f1f1;
    --card: #1c1c1c;
    --card-edge: #242424;
    --gold: #d8b25c;
    --gold-light: #f0d27e;
    --gold-deep: #a67c2e;
    --ink: #2a2112;
  }
  * { box-sizing: border-box; margin: 0; padding: 0; }
  html, body {
    width: 1200px; height: 429px; overflow: hidden;
    background: var(--backdrop);
    font-family: "Josefin Sans", sans-serif;
  }
  .canvas { position: relative; width: 1200px; height: 429px; }

  .card {
    position: absolute; top: 46px;
    width: 497px; height: 284px;
    background: linear-gradient(135deg, var(--card-edge), var(--card) 60%);
    overflow: hidden;
  }
  .card--front { left: 50px; }
  .card--back { left: 646px; }

  /* Front */
  .brand-seal {
    position: absolute; left: 165px; top: 32px;
    width: 168px; height: 168px;
    border: 1.5px solid var(--gold); border-radius: 50%;
    display: flex; align-items: center; justify-content: center;
  }
  .brand-seal__name {
    color: var(--gold); font-weight: 400; font-size: 15px;
    letter-spacing: 3px; text-transform: uppercase; text-align: center;
    line-height: 1.5;
  }
  .web-band {
    position: absolute; left: 0; top: 222px; width: 100%; height: 25px;
    background: linear-gradient(90deg, var(--gold-deep), var(--gold-light) 25%, var(--gold) 55%, var(--gold-deep));
    display: flex; align-items: center; justify-content: center;
  }
  .web-band__url {
    color: var(--ink); font-size: 11px; font-weight: 600;
    letter-spacing: 3.6px; text-transform: uppercase; padding-top: 2px;
  }

  /* Back */
  .back-brand {
    position: absolute; right: 16px; top: 20px;
    color: var(--gold); font-size: 15px; letter-spacing: 2.6px;
    text-transform: uppercase;
  }
  .profile-tab {
    position: absolute; left: 56px; top: 0; width: 26px; height: 103px;
  }
  .person {
    position: absolute; left: 93px; top: 62px; color: var(--gold);
  }
  .person__name { font-size: 30px; line-height: 1; white-space: nowrap; }
  .person__first { font-weight: 600; }
  .person__last { font-weight: 300; }
  .person__title { font-size: 12px; margin-top: 6px; }

  .contact { position: absolute; left: 0; top: 0; width: 100%; height: 100%; }
  .contact__icon { position: absolute; width: 27px; height: 32px; }
  .contact__icon--phone { left: 42px; top: 143px; }
  .contact__icon--mail { left: 55px; top: 173px; }
  .contact__icon--web { left: 42px; top: 204px; }
  .contact__text {
    position: absolute; left: 93px; color: var(--gold);
    white-space: nowrap; line-height: 1;
  }
  .contact__text--phone { top: 151px; font-size: 17px; }
  .contact__text--mail { top: 181px; font-size: 16px; }
  .contact__text--web { top: 212px; font-size: 16px; }
</style>
</head>
<body>
<main class="canvas">

  <section class="card card--front" aria-label="Business card front">
    <div class="brand-seal">
      <p class="brand-seal__name">Riverlume<br>Honey</p>
    </div>
    <div class="web-band">
      <span class="web-band__url">www.riverlumehoney.example</span>
    </div>
  </section>

  <section class="card card--back" aria-label="Business card back">
    <p class="back-brand">Riverlume Honey</p>

    <svg class="profile-tab" viewBox="0 0 26 103" aria-hidden="true">
      <defs>
        <linearGradient id="tabGold" x1="0" x2="1">
          <stop offset="0" stop-color="#a67c2e"/>
          <stop offset="0.45" stop-color="#f0d27e"/>
          <stop offset="1" stop-color="#a67c2e"/>
        </linearGradient>
      </defs>
      <path d="M0 0H26V97L13 103L0 97Z" fill="url(#tabGold)"/>
      <circle cx="13" cy="68" r="5" fill="#1c1c1c"/>
      <path d="M5 88Q5 76 13 76Q21 76 21 88Z" fill="#1c1c1c"/>
    </svg>

    <div class="person">
      <p class="person__name"><span class="person__first">Mattias</span> <span class="person__last">Brovell</span></p>
      <p class="person__title">Creative Director</p>
    </div>

    <div class="contact">
      <svg class="contact__icon contact__icon--phone" viewBox="0 0 28 32" aria-hidden="true">
        <path d="M14 1L27 8.5V23.5L14 31L1 23.5V8.5Z" fill="none" stroke="#d8b25c" stroke-width="1.4"/>
        <path d="M9.5 9.5l2.5-.5 1.5 3.5-1.6 1.1a8 8 0 0 0 3.5 3.5l1.1-1.6 3.5 1.5-.5 2.5c-5 .8-10.8-5-10-10z" fill="#d8b25c"/>
      </svg>
      <span class="contact__text contact__text--phone">+64 2919 58 617</span>

      <svg class="contact__icon contact__icon--mail" viewBox="0 0 28 32" aria-hidden="true">
        <path d="M14 1L27 8.5V23.5L14 31L1 23.5V8.5Z" fill="none" stroke="#d8b25c" stroke-width="1.4"/>
        <rect x="7" y="11" width="14" height="10" fill="#d8b25c"/>
        <path d="M7 11L14 17L21 11M7 21L12 16M21 21L16 16" fill="none" stroke="#1c1c1c" stroke-width="1"/>
      </svg>
      <span class="contact__text contact__text--mail">mattias@riverlumehoney.example</span>

      <svg class="contact__icon contact__icon--web" viewBox="0 0 28 32" aria-hidden="true">
        <path d="M14 1L27 8.5V23.5L14 31L1 23.5V8.5Z" fill="none" stroke="#d8b25c" stroke-width="1.4"/>
        <g fill="none" stroke="#d8b25c" stroke-width="1.1">
          <circle cx="14" cy="16" r="7"/>
          <ellipse cx="14" cy="16" rx="3" ry="7"/>
          <path d="M7 16H21M8 12.5H20M8 19.5H20"/>
        </g>
      </svg>
      <span class="contact__text contact__text--web">mattias@riverlumehoney.example</span>
    </div>
  </section>

</main>
</body>
</html>
```